Orbel Appraisals website redesign

I would like to refresh my existing website of www.orbelappraisals-demo.com with new graphics, look and feel, as well as updated structure and wording. Content and layout changes have been uploaded to this project Brief.

My existing website has a dark feel. I am now looking for a light and energetic feel. Financial Services is my industry, so the website should be reflect that. I would also like to reflect the concepts of Trust, Service and Expertise.

The website must be serious and upmarket.

Target Market(s)

Corporate board members, CFO's, treasurers and controllers
Auditors, tax advisors, private equity and venture capital asset managers, investors, tax authorities

Industry/Entity Type

Financial Service

Coding

Coded - Design and coding required

Number of Pages Required

5+ page

Font styles to use
Sans Serif
Other font styles liked:
• Designer can choose another modern font

Colors
0355a3
3277b5
85acd3
eaf1f7
f37122
f68d4d
9bcb3c
acd037
cadf82

Requirements
Must have
• Good hi resolution pictures that convey "Finance", "Trust", "Service" or "Expertise".
• An anti-bot (such as Captcha) mechanism in the contact form.
Should not have
• Must not have all content on one rolling screen.

```html
<!DOCTYPE html>
<html lang="en">
<head>
<meta charset="utf-8">
<title>Orbel Appraisals</title>
<link href="https://fonts.googleapis.com/css2?family=Montserrat:ital,wght@0,400;0,500;0,600;0,700;1,400&display=swap" rel="stylesheet">
<style>
:root{
  --blue:#0355a3;
  --blue-mid:#3277b5;
  --blue-light:#85acd3;
  --pale:#eef2f8;
  --orange:#f37122;
  --orange-light:#f68d4d;
  --ink:#0b1a3a;
  --body:#3a4257;
  --muted:#6b7388;
  --white:#ffffff;
}
*{box-sizing:border-box;margin:0;padding:0}
html,body{width:1200px;height:2844px;overflow:hidden}
body{font-family:'Montserrat',sans-serif;color:var(--ink);background:var(--white);position:relative}
.abs{position:absolute}

/* hero */
.hero{position:absolute;left:0;top:0;width:1200px;height:600px;overflow:hidden}
.hero-photo{position:absolute;inset:0;background:linear-gradient(180deg,#1a1a1c 0%,#4a4b4f 35%,#8a8c90 60%,#5a5b5e 100%)}
.hero-shade{position:absolute;inset:0;background:radial-gradient(ellipse at 50% 40%,rgba(180,182,186,.35),rgba(0,0,0,.3) 70%)}
.hero-curve{position:absolute;left:0;top:0}
.brand{position:absolute;left:234px;top:54px;color:var(--white);font-weight:500;font-size:19px;letter-spacing:1px}
.nav{position:absolute;top:48px;right:240px;display:flex;gap:38px}
.nav a{color:var(--white);font-size:11px;font-weight:700;letter-spacing:.5px;text-decoration:none}
.nav a.active{color:var(--orange)}
.play{position:absolute;left:572px;top:155px;width:54px;height:54px;border:2px solid var(--white);border-radius:50%}
.play svg{position:absolute;left:19px;top:17px}
.hero-title{position:absolute;left:0;width:1200px;top:226px;text-align:center;color:var(--white);font-weight:700;font-size:36px;line-height:40px;letter-spacing:1px}
.slider{position:absolute;left:793px;top:391px;width:228px;height:12px}

/* section heads */
.section-title{position:absolute;left:0;width:1200px;text-align:center;font-weight:600;font-size:22px;letter-spacing:1px;color:var(--ink)}
.rule{position:absolute;left:582px;width:36px;height:2px;background:#7b8296}

/* values */
.values{position:absolute;left:0;top:450px;width:1200px;height:431px;background:linear-gradient(90deg,#f2f3f6,#fbfbfc 40%,#f1f2f5 100%)}
.value{position:absolute}
.value svg{position:absolute;left:0;top:0}
.value h3{position:absolute;font-size:16px;font-weight:600;letter-spacing:.5px;color:var(--ink)}
.value p{position:absolute;font-size:9.5px;line-height:15px;color:var(--body);width:500px}

/* services */
.services{position:absolute;left:0;top:881px;width:1200px;height:957px;background:var(--pale)}
.card{position:absolute;width:231px;height:298px;background:var(--white);box-shadow:0 2px 8px rgba(20,40,80,.06)}
.card .photo{height:148px}
.card h4{margin:24px 16px 0;text-align:center;font-size:11.5px;font-weight:600;line-height:16px;color:var(--ink);letter-spacing:.2px}
.card p{margin:8px 20px 0;text-align:center;font-size:10.5px;line-height:16px;color:var(--body)}
.card .go{position:absolute;left:97px;bottom:-18px;width:36px;height:36px;border-radius:50%;background:var(--orange);box-shadow:0 3px 8px rgba(243,113,34,.35)}
.card .go svg{position:absolute;left:11px;top:12px}

/* news */
.news{position:absolute;left:0;top:1838px;width:1200px;height:640px}
.news-bg{position:absolute;inset:0;background:linear-gradient(120deg,#f6f6f7,#ffffff 45%,#f3f4f5)}
.post{position:absolute;width:231px}
.post .photo{height:202px;margin-bottom:24px}
.post time{display:block;font-size:9px;font-style:italic;color:var(--muted)}
.post h5{font-size:14px;font-weight:500;line-height:19px;color:var(--ink);margin-top:10px}
.post .authors{font-size:9px;font-weight:600;color:var(--blue);line-height:15px;margin-top:12px}
.post .excerpt{font-size:9px;line-height:15px;color:var(--body);text-align:justify;margin-top:12px}
.more{position:absolute;font-size:9px;font-weight:600;color:var(--orange);text-decoration:underline;letter-spacing:.3px}

/* footer */
.footer{position:absolute;left:0;top:2420px;width:1200px;height:424px}
.footer-curve{position:absolute;left:0;top:0}
.f-head{position:absolute;font-size:11.5px;font-weight:700;color:var(--white);letter-spacing:.5px}
.f-sub{position:absolute;font-size:11px;font-weight:600;color:var(--white)}
.f-text{position:absolute;font-size:9px;line-height:16px;color:#d7e3f2}
.f-icon{position:absolute;width:18px;height:18px;border:1px solid #9fbde0;border-radius:50%}
.f-icon svg{position:absolute;left:4px;top:3px}
.badge{position:absolute;background:rgba(255,255,255,.9);border-radius:4px}
.f-line{position:absolute;left:234px;top:351px;width:732px;height:1px;background:#3b72b3}
.copy{position:absolute;left:0;width:1200px;top:382px;text-align:center;font-size:8.5px;color:#d7e3f2}
</style>
</head>
<body>

<header class="hero">
  <div class="hero-photo" role="img" aria-label="Looking up at city skyscrapers, greyscale"></div>
  <div class="hero-shade"></div>
  <svg class="hero-curve" width="1200" height="600" viewBox="0 0 1200 600">
    <path d="M0,488 C140,410 300,380 470,384 C680,390 860,458 1010,442 C1110,432 1170,395 1200,350 L1200,600 L0,600 Z" fill="var(--orange)"/>
    <path d="M0,545 C160,440 320,400 490,405 C700,412 860,470 1010,455 C1110,445 1170,405 1200,364 L1200,600 L0,600 Z" fill="#f2f3f6"/>
  </svg>
  <div class="brand">ORBEL APPRAISALS</div>
  <nav class="nav">
    <a class="active" href="#">HOME</a><a href="#">ABOUT</a><a href="#">SERVICES</a><a href="#">NEWS &amp; VIEWS</a><a href="#">CONTACT</a>
  </nav>
  <div class="play"><svg width="16" height="18" viewBox="0 0 16 18"><path d="M0,0 L15,9 L0,18 Z" fill="#fff"/></svg></div>
  <h1 class="hero-title">BUSINESS &amp; INTELLECTUAL<br>PROPERTY VALUATIONS</h1>
  <svg class="slider" viewBox="0 0 228 12">
    <line x1="6" y1="6" x2="226" y2="6" stroke="#c9cbcf" stroke-width="1"/>
    <circle cx="6" cy="6" r="5.5" fill="#d6d7da"/><circle cx="6" cy="6" r="2.5" fill="#fff"/>
    <circle cx="76" cy="6" r="2.5" fill="none" stroke="#d6d7da"/>
    <circle cx="151" cy="6" r="2.5" fill="none" stroke="#d6d7da"/>
    <circle cx="226" cy="6" r="2.5" fill="none" stroke="#d6d7da"/>
  </svg>
</header>

<section class="values">
  <h2 class="section-title" style="top:72px">TRUST, SERVICE &amp; EXPERTISE</h2>
  <div class="rule" style="top:112px"></div>

  <div class="value" style="left:322px;top:140px">
    <svg width="56" height="60" viewBox="0 0 56 60"><path d="M28,2 L53,16 L53,44 L28,58 L3,44 L3,16 Z" fill="var(--blue)"/><path d="M28,16 L40,20 L40,30 C40,38 34,43 28,46 C22,43 16,38 16,30 L16,20 Z" fill="none" stroke="#fff" stroke-width="2"/><path d="M22,30 L26.5,34.5 L34,26" fill="none" stroke="#fff" stroke-width="2.4"/></svg>
    <h3 style="left:71px;top:10px">TRUST</h3>
    <p style="left:71px;top:31px">Trust is paramount. Clients rely on Orbel Appraisals for confidentiality, transparency and independence.</p>
  </div>
  <div class="value" style="left:393px;top:214px">
    <svg width="56" height="60" viewBox="0 0 56 60"><path d="M28,2 L53,16 L53,44 L28,58 L3,44 L3,16 Z" fill="var(--blue)"/><circle cx="21" cy="22" r="4" fill="none" stroke="#fff" stroke-width="1.6"/><circle cx="35" cy="22" r="4" fill="none" stroke="#fff" stroke-width="1.6"/><circle cx="21" cy="38" r="4" fill="none" stroke="#fff" stroke-width="1.6"/><circle cx="35" cy="38" r="4" fill="none" stroke="#fff" stroke-width="1.6"/><path d="M25,22 L31,22 M21,26 L21,34 M35,26 L35,34" stroke="#fff" stroke-width="1.4"/></svg>
    <h3 style="left:71px;top:10px">SERVICE</h3>
    <p style="left:71px;top:36px">Service is front and center at Orbel Appraisals. We consider the needs of all stakeholders and the personal needs of the client team involved.</p>
  </div>
  <div class="value" style="left:463px;top:308px">
    <svg width="56" height="60" viewBox="0 0 56 60"><path d="M28,2 L53,16 L53,44 L28,58 L3,44 L3,16 Z" fill="var(--blue)"/><rect x="16" y="20" width="24" height="18" rx="2" fill="none" stroke="#fff" stroke-width="1.6"/><path d="M23,20 L23,16 L33,16 L33,20 M16,28 L40,28" stroke="#fff" stroke-width="1.6" fill="none"/></svg>
    <h3 style="left:71px;top:10px">EXPERTISE</h3>
    <p style="left:71px;top:36px">Expertise is core to the philosophy of Orbel Appraisals. Our global network of professionals maintain and continue to develop the knowledge and experience that you expect from your trusted corporate finance partner.</p>
  </div>
</section>

<section class="services">
  <h2 class="section-title" style="top:119px">OUR SERVICES</h2>
  <div class="rule" style="top:159px"></div>

  <article class="card" style="left:234px;top:209px">
    <div class="photo" role="img" aria-label="Hands with a calculator and pen over financial reports" style="background:linear-gradient(135deg,#d9e0ea,#9fb0c6 60%,#e8ecf1)"></div>
    <h4>BUSINESS VALUATION</h4>
    <p>Company stakeholders trust Orbel Appraisals to provide business valuations for transaction, accounting, tax, legal, and share or option</p>
    <span class="go"><svg width="14" height="12" viewBox="0 0 14 12"><path d="M1,6 L12,6 M7,1 L12,6 L7,11" fill="none" stroke="#fff" stroke-width="1.6"/></svg></span>
  </article>
  <article class="card" style="left:485px;top:209px">
    <div class="photo" role="img" aria-label="Business hands holding a glowing brain symbol" style="background:linear-gradient(135deg,#0c1420,#1c2a3c 55%,#0a6f86 75%,#0b1520)"></div>
    <h4>INTELLECTUAL PROPERTY VALUATION</h4>
    <p>Patents, unpatented technologies, know how, brands, trademarks, databases, customer-related assets</p>
    <span class="go"><svg width="14" height="12" viewBox="0 0 14 12"><path d="M1,6 L12,6 M7,1 L12,6 L7,11" fill="none" stroke="#fff" stroke-width="1.6"/></svg></span>
  </article>
  <article class="card" style="left:734px;top:209px">
    <div class="photo" role="img" aria-label="Two businessmen reviewing documents in an office" style="background:linear-gradient(135deg,#cfd6df,#5a6a7c 55%,#2f3b4a)"></div>
    <h4>M&amp;A ADVISORY</h4>
    <p>Through our international network of M&amp;A professionals, Orbel Appraisals can assist companies with buying other companies or selling</p>
    <span class="go"><svg width="14" height="12" viewBox="0 0 14 12"><path d="M1,6 L12,6 M7,1 L12,6 L7,11" fill="none" stroke="#fff" stroke-width="1.6"/></svg></span>
  </article>
  <article class="card" style="left:359px;top:555px">
    <div class="photo" role="img" aria-label="Team planning session with sticky notes on a wall" style="background:linear-gradient(135deg,#e9e6e1,#b9b4ac 55%,#f0ece4)"></div>
    <h4>BUSINESS PLAN COACHING</h4>
    <p>Young companies and entrepreneurs frequently ask for our advice on their business plans and strategies. With almost 2 decades</p>
    <span class="go"><svg width="14" height="12" viewBox="0 0 14 12"><path d="M1,6 L12,6 M7,1 L12,6 L7,11" fill="none" stroke="#fff" stroke-width="1.6"/></svg></span>
  </article>
  <article class="card" style="left:609px;top:555px">
    <div class="photo" role="img" aria-label="Hand signing a document beside charts" style="background:linear-gradient(135deg,#e6ecf3,#aebfd4 55%,#f3f5f8)"></div>
    <h4>PURCHASE PRICE ALLOCATION</h4>
    <p>Accounting procedures require an acquiror to allocate purchase consideration to the fair value of all acquired assets and liabilities</p>
    <span class="go"><svg width="14" height="12" viewBox="0 0 14 12"><path d="M1,6 L12,6 M7,1 L12,6 L7,11" fill="none" stroke="#fff" stroke-width="1.6"/></svg></span>
  </article>
</section>

<section class="news">
  <div class="news-bg" role="img" aria-label="Faded desk with laptop and business newspaper"></div>
  <h2 class="section-title" style="top:120px">LATEST NEWS</h2>

  <article class="post" style="left:234px;top:212px">
    <div class="photo" role="img" aria-label="Street sign at a stock exchange" style="background:linear-gradient(180deg,#6e7073,#2a2b2d 45%,#b9bbbe 70%,#9a9c9f)"></div>
    <time>February 18, 2019</time>
    <h5>Martin Hollis to Speak at Bridge2West on Feb 18 in Oosterhout, the Netherlands</h5>
  </article>
  <a class="more" style="left:234px;top:532px">READ MORE</a>

  <article class="post" style="left:484px;top:215px">
    <time>March 9, 2016</time>
    <h5>Dutch GAAP Update – Goodwill and Definitions of Value</h5>
    <div class="authors">Martin K. Hollis, CFA, ASA, RV<br>Pieter J. Valkema</div>
    <p class="excerpt">A number of Dutch GAAP accounting changes took effect on January 1, 2016, some of which affect goodwill and definitions of value. This paper briefly discusses the updates to goodwill and definitions of value and assumes a practitioner's understanding on basic definitions of value. Please do not hesitate to let us know if you would like further information.</p>
    <p class="excerpt">The recently published 2015 edition of the Dutch GAAP accounting handbook "Richtlijnen voor de jaarverslaggeving voor grote en middelgrote rechtspersonen" includes some key changes affecting goodwill.</p>
  </article>
  <a class="more" style="left:484px;top:532px">READ MORE</a>

  <article class="post" style="left:734px;top:212px">
    <div class="photo" role="img" aria-label="Street sign at a stock exchange" style="background:linear-gradient(180deg,#6e7073,#2a2b2d 45%,#b9bbbe 70%,#9a9c9f)"></div>
    <time>February 18, 2019</time>
    <h5>Orbel Appraisals presenteert bij Bridge2West op 18 februari in Oosterhout</h5>
  </article>
  <a class="more" style="left:734px;top:532px">READ MORE</a>
</section>

<footer class="footer">
  <svg class="footer-curve" width="1200" height="424" viewBox="0 0 1200 424">
    <path d="M0,20 C120,80 260,110 430,100 C640,88 820,20 960,10 C1080,2 1160,40 1200,70 L1200,424 L0,424 Z" fill="var(--orange)"/>
    <path d="M0,0 C140,70 280,100 450,92 C650,82 820,30 960,26 C1080,22 1160,80 1200,118 L1200,424 L0,424 Z" fill="var(--blue)"/>
  </svg>
  <div class="f-head" style="left:234px;top:172px">ABOUT US</div>
  <p class="f-text" style="left:234px;top:196px;width:232px">Orbel Appraisals, founded in 2012, is a boutique valuation advisory practice servicing companies throughout Europe and North America. We have offices in Leiden and Amsterdam. Through our affiliate partners, we also have offices in New York and London offering transfer pricing, derivatives modelling, and machinery &amp; equipment valuation.</p>

  <div class="f-head" style="left:503px;top:172px">LOCATIONS</div>
  <div class="f-sub" style="left:503px;top:200px">Leiden</div>
  <div class="f-sub" style="left:634px;top:200px">Amsterdam</div>
  <span class="f-icon" style="left:505px;top:230px"><svg width="10" height="12" viewBox="0 0 10 12"><path d="M5,11 C2,7 1,5.5 1,4 A4,4 0 0 1 9,4 C9,5.5 8,7 5,11 Z" fill="none" stroke="#cfe0f3"/><circle cx="5" cy="4" r="1.3" fill="#cfe0f3"/></svg></span>
  <p class="f-text" style="left:532px;top:228px">Kanaalweg 118<br>2321 AB Leiden</p>
  <span class="f-icon" style="left:505px;top:270px"><svg width="10" height="12" viewBox="0 0 10 12"><path d="M2,1 L4,1 L5,4 L3.5,5 C4,7 5,8 7,8.5 L8,7 L10,8 L10,10 C5,11 1,6 2,1 Z" fill="none" stroke="#cfe0f3"/></svg></span>
  <p class="f-text" style="left:532px;top:271px">070 555 0142</p>
  <span class="f-icon" style="left:636px;top:230px"><svg width="10" height="12" viewBox="0 0 10 12"><path d="M5,11 C2,7 1,5.5 1,4 A4,4 0 0 1 9,4 C9,5.5 8,7 5,11 Z" fill="none" stroke="#cfe0f3"/><circle cx="5" cy="4" r="1.3" fill="#cfe0f3"/></svg></span>
  <p class="f-text" style="left:662px;top:228px">Zuidplein 45<br>1077 XV Amsterdam</p>
  <span class="f-icon" style="left:636px;top:270px"><svg width="10" height="12" viewBox="0 0 10 12"><path d="M2,1 L4,1 L5,4 L3.5,5 C4,7 5,8 7,8.5 L8,7 L10,8 L10,10 C5,11 1,6 2,1 Z" fill="none" stroke="#cfe0f3"/></svg></span>
  <p class="f-text" style="left:662px;top:271px">020 555 0187</p>

  <div class="badge" style="left:799px;top:168px;width:140px;height:28px"></div>
  <div class="badge" style="left:799px;top:222px;width:141px;height:58px"></div>

  <div class="f-line"></div>
  <p class="copy">Copyright © 2019 Orbel Appraisals. All rights reserved | Privacy Policy</p>
</footer>

</body>
</html>
```